Brochure for Upscale Painting and Contractor Services Company

We are a higher end interior and exterior painting contractor which also provides a range of other services as found on www.brindlecoatfinishes.net. Our edge in the market is being the "gentlemen painters" as we are clean shaven, kind to all customers, clean up more than we received it, timely with everything and do the best work around at the right price.

We need a brochure that reflects the elegance and quality of work we perform. We really want this to have a folder within to actually insert a letter and printed proposal from our founder so we can present on the spot or add flyers to and hand out at events, etc. We want something full page so no trifolds, rather a bifold with some means of have a folder insert.

The design should be elegant but bold with images.

Target Market(s)

We are typically working with women between 45-55 years of age living in homes worth $500K to $1m. You can imagine what they like (need) to see from contractors and we are already elegant and serving that need with our web and online communications but we need a print piece to match.

Industry/Entity Type

Painting

```html
<!DOCTYPE html>
<html lang="en">
<head>
<meta charset="utf-8">
<title>Brindlecoat Finishes – Prices &amp; Portfolio</title>
<link href="https://fonts.googleapis.com/css2?family=Source+Sans+3:wght@300;400&display=swap" rel="stylesheet">
<style>
  :root {
    --page-white: #ffffff;
    --portfolio-grey: #6b6b70;
    --body-grey: #6a6a6a;
    --oxblood: #5e1a0e;
    --oxblood-head: #6b1a0c;
    --label-light: #e6e6e6;
    --title-light: #d9d9db;
  }
  * { margin: 0; padding: 0; box-sizing: border-box; }
  html, body { width: 1200px; height: 848px; overflow: hidden; background: var(--page-white); }
  body { font-family: "Source Sans 3", sans-serif; position: relative; }
  .spread { position: relative; width: 1200px; height: 848px; }
  .page-left { position: absolute; left: 0; top: 0; width: 600px; height: 848px; background: var(--page-white); }
  .page-right { position: absolute; left: 600px; top: 0; width: 600px; height: 848px; background: var(--portfolio-grey); }
  .photo { position: absolute; }
  .hero-room { left: 40px; top: 66px; width: 372px; height: 208px;
    background: linear-gradient(160deg, #6e625d 0%, #8a7f7a 35%, #d8d6d2 55%, #2a2a2a 85%, #111 100%); }
  .hero-roller { left: 417px; top: 66px; width: 183px; height: 209px;
    background: linear-gradient(180deg, #dfe6b8 0%, #c9d49a 40%, #4f5f78 65%, #e6d9c5 100%); }
  .prices-title { position: absolute; left: 46px; top: 230px; font-size: 30px; font-weight: 300; color: #fff; }
  .intro { position: absolute; left: 46px; width: 508px; font-size: 10.6px; line-height: 14.5px;
    font-weight: 300; color: var(--body-grey); text-align: justify; }
  .intro-one { top: 302px; }
  .intro-two { top: 374px; }
  .painter { left: 40px; top: 452px; width: 230px; height: 396px;
    background: linear-gradient(180deg, #f4f4f4 0%, #e9e6e2 40%, #f2f2f2 100%); }
  .checklist-title { position: absolute; left: 291px; top: 451px; font-size: 22.5px; line-height: 21px;
    font-weight: 400; color: var(--oxblood-head); }
  .checklist { position: absolute; left: 271px; top: 497px; width: 329px; height: 284px;
    background: var(--oxblood); list-style: none; padding: 14px 40px 0 21px; }
  .checklist li { color: #fff; font-size: 12px; line-height: 15.5px; font-weight: 400; height: 47px; }
  .folio-no { position: absolute; left: 26px; top: 822px; font-size: 8px; color: #999; }

  .portfolio-title { position: absolute; left: 66px; top: 80px; font-size: 31px; font-weight: 300; color: var(--title-light); }
  .label { position: absolute; font-size: 12px; font-weight: 400; color: var(--label-light); letter-spacing: 0.2px; }
  .thumb { position: absolute; width: 117px; height: 105px; box-shadow: 2px 3px 4px rgba(0,0,0,0.35); }
  .tone-warm { background: linear-gradient(160deg, #c9a86a, #e9d49c 50%, #8a6a38); }
  .tone-red { background: linear-gradient(160deg, #6b2a24, #c7c4b0 55%, #4b4b3a); }
  .tone-blue { background: linear-gradient(160deg, #3f5a6a, #8a9aa2 55%, #7a5d4a); }
  .tone-house { background: linear-gradient(180deg, #9fb08a, #c8c3b8 45%, #6e6254); }
  .tone-sky { background: linear-gradient(180deg, #6a8fc8, #b9c9dc 50%, #c96a6a); }
  .tone-white-house { background: linear-gradient(180deg, #5e7a4a, #e4e6ea 45%, #c9cdd4); }
  .tone-wood { background: linear-gradient(90deg, #5e4a3a, #a0785a 50%, #6a5040); }
  .tone-siding { background: linear-gradient(180deg, #dfe3e6, #a9b0b6 60%, #6e7a5a); }
  .tone-spray { background: linear-gradient(180deg, #5a2a1a, #b5532a 45%, #6a6f8a); }
  .tone-ceiling { background: linear-gradient(180deg, #b7aa98, #e2ddd4 50%, #8a7e70); }
  .tone-deck { background: linear-gradient(180deg, #3a5a2a, #cfd6df 45%, #8a96a6); }
  .tone-paper-red { background: linear-gradient(160deg, #e8d8c8, #c46a6a 45%, #f2ece4); }
  .tone-paper-lilac { background: linear-gradient(180deg, #c9bfd6, #e2dcea 70%, #2a2a2a); }
  .tone-paper-hand { background: linear-gradient(160deg, #e6e6da, #c9c7b8 55%, #3a3020); }
</style>
</head>
<body>
<div class="spread">
  <section class="page-left">
    <div class="photo hero-room" role="img" aria-label="Modern living room with white wall units and dark sofa"></div>
    <div class="photo hero-roller" role="img" aria-label="Painter in jeans rolling green paint on a wall"></div>
    <h1 class="prices-title">Our Prices</h1>
    <p class="intro intro-one">We are very sensitive to the cost of our services and feel transparency with our customers is the key to success. We strive to not only provide the highest quality services but we never settle for less than 100% customer satisfaction. This requires a high level of training and skills for our team members, hiring only those who fit the profile of what we expect from our gentlemen painters.</p>
    <p class="intro intro-two">We firmly believe we are the best painters in the area. The old adage “you get what you pay for” is true, but we believe you get more than what you pay for here at Brindlecoat. We will not always be the cheapest but relative to any alternative, we are the best value for money, hands down. We stand by our work and are worth every penny you will spend.</p>
    <div class="photo painter" role="img" aria-label="Smiling painter in white cap holding a paint roller"></div>
    <h2 class="checklist-title">What to look for<br>in a contractor ?</h2>
    <ul class="checklist">
      <li>Can they provide evidence of being licensed and insured?</li>
      <li>Are they employing legally documented workers?</li>
      <li>Have they conducted a background investigation on their employees?</li>
      <li>If comparing quotes, be sure to compare apples to apples.</li>
      <li>What is the history of the company? Do they have referrals?</li>
      <li>Are they responsive?</li>
    </ul>
    <span class="folio-no">4</span>
  </section>

  <section class="page-right">
    <h2 class="portfolio-title">Portfolio</h2>

    <span class="label" style="left:63px;top:140px">INTERIOR PAINTING</span>
    <div class="thumb tone-warm" style="left:63px;top:158px" role="img" aria-label="Freshly painted warm yellow basement"></div>
    <div class="thumb tone-red" style="left:185px;top:158px" role="img" aria-label="Living room with red accent wall"></div>
    <div class="thumb tone-blue" style="left:306px;top:158px" role="img" aria-label="Bedroom painted slate blue"></div>

    <span class="label" style="left:429px;top:137px">EXTERIOR PAINTING</span>
    <div class="thumb tone-house" style="left:428px;top:158px" role="img" aria-label="Stone and siding house with porch"></div>
    <div class="thumb tone-sky" style="left:428px;top:268px" role="img" aria-label="Blue painted house facade"></div>
    <div class="thumb tone-white-house" style="left:428px;top:376px" role="img" aria-label="White colonial house entrance"></div>

    <span class="label" style="left:63px;top:286px">POWERWASHING</span>
    <div class="thumb tone-wood" style="left:63px;top:308px" role="img" aria-label="Deck boards before and after washing"></div>
    <div class="thumb tone-siding" style="left:185px;top:308px" role="img" aria-label="Grey siding being washed"></div>
    <div class="thumb tone-spray" style="left:306px;top:308px" role="img" aria-label="Pressure washer spraying a surface"></div>

    <div class="thumb tone-ceiling" style="left:63px;top:417px" role="img" aria-label="Worker repairing a ceiling"></div>
    <div class="thumb tone-ceiling" style="left:185px;top:417px" role="img" aria-label="Worker finishing drywall near a window"></div>
    <span class="label" style="left:306px;top:461px">DRYWALL SERVICES</span>

    <div class="thumb tone-deck" style="left:63px;top:529px" role="img" aria-label="Sealed deck with white railings"></div>
    <div class="thumb tone-deck" style="left:63px;top:638px" role="img" aria-label="Stained deck staircase"></div>
    <span class="label" style="left:183px;top:579px">STAINING &amp; SEALING</span>

    <div class="thumb tone-paper-red" style="left:311px;top:542px;height:115px" role="img" aria-label="Red patterned wallpaper around a doorway"></div>
    <div class="thumb tone-paper-lilac" style="left:432px;top:542px;height:115px" role="img" aria-label="Lilac patterned wallpaper in a bedroom"></div>
    <div class="thumb tone-paper-hand" style="left:432px;top:661px;height:116px" role="img" aria-label="Hand trimming wallpaper around an outlet"></div>
    <span class="label" style="left:345px;top:691px">WALLPAPER</span>
  </section>
</div>
</body>
</html>
```